Business Card Design

I'm a young beekeeper (22 years old) just starting out. I own and run 80 hives and would like to eventually build up to 1000. My aim is to run it in tandem with our family farm that is currently running sheep and beef. Unlike a number of honey companies on the East Coast (or the North Island, NZ) I am local and will expand onto the lease blocks that our family is also leasing. I want a simple plain logo/photo. The designer may wish to use one of the photos as a background outline or however they chose. The mountain is Aorangi and our farm borders one side of it.

Target Market(s)

From local land owners to wholesale honey buyers

Industry/Entity Type

Farm

Contact Information for Business Card

Pekeriu Honey
Manager Owner Manaia Brooks
email pekeriuhoney@tuimailbox.co.nz
mobile 0217394461

Requirements
Must have
• The details submitted. The brand Pekeriu Honey to be the main feature. The other details can be smaller.
Should not have
• Must not include a picture of a bee or hive. Use a modern font. Don't use koru but may incorporate poutama.

```html
<!DOCTYPE html>
<html lang="en">
<head>
<meta charset="utf-8">
<title>Pekeriu Honey – Business Cards</title>
<link rel="stylesheet" href="https://fonts.googleapis.com/css2?family=Open+Sans:wght@400;700&display=swap">
<style>
  :root {
    --canvas: #ffffff;
    --ink: #111111;
    --ink-light: #ffffff;
    --sky: #eef4f7;
    --sky-blue: #cfe3ee;
    --mountain: #4a5560;
    --mountain-deep: #343f44;
    --forest: #3d4737;
    --grass: #7e7a4c;
    --grass-light: #948d5c;
    --sun: rgba(250, 240, 40, 0.95);
    --sun-soft: rgba(250, 240, 40, 0);
    --shadow: rgba(0, 0, 0, 0.55);
  }
  * { margin: 0; padding: 0; box-sizing: border-box; }
  html, body {
    width: 1200px;
    height: 1000px;
    overflow: hidden;
    background: var(--canvas);
    font-family: "Open Sans", Arial, sans-serif;
  }
  .canvas { position: relative; width: 1200px; height: 1000px; }

  .card {
    position: absolute;
    overflow: hidden;
    background: var(--canvas);
    box-shadow: 6px 7px 6px var(--shadow);
  }
  .card--portrait { left: 142px; top: 208px; width: 343px; height: 554px; }
  .card--landscape { left: 526px; top: 313px; width: 555px; height: 343px; }

  .landscape-photo { position: absolute; left: 0; top: 0; width: 100%; }
  .card--portrait .landscape-photo {
    height: 402px;
    background:
      radial-gradient(ellipse 120px 160px at 100% 95%, var(--sun), var(--sun-soft)),
      linear-gradient(180deg, var(--sky) 0%, var(--sky-blue) 12%, #e9eef0 22%, var(--mountain) 27%, var(--mountain-deep) 48%, var(--forest) 60%, var(--grass) 72%, var(--grass-light) 88%, var(--grass) 100%);
  }
  .card--landscape .landscape-photo {
    height: 100%;
    background:
      radial-gradient(ellipse 200px 220px at 100% 38%, var(--sun), var(--sun-soft)),
      linear-gradient(180deg, var(--sky-blue) 0%, var(--sky) 20%, #e6ecee 28%, var(--mountain) 34%, var(--mountain-deep) 62%, var(--forest) 76%, var(--grass) 84%, var(--grass-light) 95%, var(--grass) 100%);
  }

  .card-glow {
    position: absolute;
    left: 0; top: 402px; width: 100%; height: 152px;
    background: radial-gradient(ellipse 170px 170px at 100% 0%, var(--sun), var(--sun-soft));
  }

  .card-details {
    position: absolute;
    left: 0; width: 100%;
    text-align: center;
  }
  .card--portrait .card-details { top: 406px; color: var(--ink); }
  .card--landscape .card-details { top: 116px; color: var(--ink-light); }

  .brand-name {
    font-weight: 700;
    font-size: 34px;
    line-height: 50px;
    letter-spacing: 0.2px;
  }
  .card--landscape .brand-name { line-height: 60px; }

  .contact-line {
    font-weight: 400;
    font-size: 17px;
    line-height: 21.5px;
  }
  .card--landscape .contact-line { font-size: 18px; line-height: 23px; }
</style>
</head>
<body>
  <main class="canvas">
    <section class="card card--portrait">
      <div class="landscape-photo" role="img" aria-label="Photograph of a rugged mountain above a sunlit grassy ridge under a pale sky"></div>
      <div class="card-glow"></div>
      <div class="card-details">
        <p class="brand-name">Pekeriu Honey</p>
        <p class="contact-line">Manaia Brooks</p>
        <p class="contact-line">pekeriuhoney@tuimailbox.co.nz</p>
        <p class="contact-line">0217394461</p>
      </div>
    </section>

    <section class="card card--landscape">
      <div class="landscape-photo" role="img" aria-label="Photograph of a rugged mountain with sun flare over a grassy ridge and forest"></div>
      <div class="card-details">
        <p class="brand-name">Pekeriu Honey</p>
        <p class="contact-line">Manaia Brooks</p>
        <p class="contact-line">pekeriuhoney@tuimailbox.co.nz</p>
        <p class="contact-line">0217394461</p>
      </div>
    </section>
  </main>
</body>
</html>
```